We are a new company with 2 divisions a medical research and medical product sales. We need a company logo and Business Cards. The design files need to be provided to us in Adobe Photoshop CS 5.1.

Target Market(s)

Medical Community

Industry/Entity Type

Medical

Contact Information for Business Card

Company Name - Larkmoor Biomedical LLC
Company Address 4217 NE 14th Ave Suite 7, Gainesville Fl 32609

Requirements
Must have
• The design files need to be provided to us in Adobe Photoshop CS 5.1.

```html
<!DOCTYPE html>
<html lang="en">
<head>
<meta charset="utf-8">
<title>Larkmoor Biomedical LLC — Business Card</title>
<link rel="stylesheet" href="https://fonts.googleapis.com/css2?family=Open+Sans:wght@400;600;700&display=swap">
<style>
  :root {
    --backdrop: #d9d9d9;
    --card-white: #ffffff;
    --brand-blue: #1e6cb8;
    --band-blue-light: #2f86cc;
    --band-blue-dark: #0d4f9c;
    --accent-red: #d0202a;
    --accent-red-dark: #9e1218;
    --text-white: #ffffff;
  }
  * { box-sizing: border-box; margin: 0; padding: 0; }
  html, body { width: 1200px; height: 900px; overflow: hidden; }
  body {
    background: var(--backdrop);
    font-family: "Open Sans", Arial, sans-serif;
    position: relative;
  }
  .business-card {
    position: absolute;
    left: 100px; top: 165px;
    width: 1000px; height: 570px;
    border-radius: 40px;
    background: var(--card-white);
    overflow: hidden;
    box-shadow: 0 10px 30px rgba(0,0,0,0.18);
  }
  .card-art { position: absolute; inset: 0; }
  .brand-lockup {
    position: absolute;
    left: 60px; top: 110px;
    display: flex; align-items: center; gap: 22px;
  }
  .brand-mark {
    width: 46px; height: 46px; border-radius: 50%;
    background: var(--accent-red);
  }
  .brand-name {
    font-weight: 700; font-size: 52px; color: var(--brand-blue);
    letter-spacing: -0.5px;
  }
  .person {
    position: absolute;
    right: 460px; top: 392px;
    text-align: right; color: var(--text-white);
  }
  .person-name { font-weight: 600; font-size: 27px; color: var(--accent-red); line-height: 1.2; }
  .person-title { font-size: 20px; line-height: 1.4; }
  .divider {
    position: absolute; left: 560px; top: 360px;
    width: 2px; height: 160px; background: var(--text-white); opacity: 0.9;
  }
  .contact-list {
    position: absolute; left: 582px; top: 355px;
    list-style: none; color: var(--text-white); font-size: 21px; line-height: 31px;
  }
  .contact-item { display: flex; align-items: flex-start; gap: 8px; }
  .contact-icon { width: 22px; height: 22px; margin-top: 5px; flex: none; }
  .contact-address { line-height: 30px; }
</style>
</head>
<body>
  <main class="business-card">
    <svg class="card-art" viewBox="0 0 1000 570" aria-hidden="true">
      <defs>
        <linearGradient id="band-gradient" x1="0" y1="0" x2="1" y2="1">
          <stop offset="0" stop-color="var(--band-blue-light)"/>
          <stop offset="1" stop-color="var(--band-blue-dark)"/>
        </linearGradient>
        <linearGradient id="swoosh-gradient" x1="0" y1="0" x2="1" y2="0">
          <stop offset="0" stop-color="var(--accent-red-dark)"/>
          <stop offset="1" stop-color="var(--accent-red)"/>
        </linearGradient>
      </defs>
      <path class="blue-band" d="M0,440 C230,320 560,260 1000,150 L1000,570 L0,570 Z" fill="url(#band-gradient)"/>
      <path class="red-swoosh" d="M540,300 C740,250 900,190 1000,55 L1000,120 C900,215 740,265 540,300 Z" fill="url(#swoosh-gradient)"/>
    </svg>

    <div class="brand-lockup">
      <span class="brand-mark"></span>
      <span class="brand-name">Larkmoor Biomedical LLC</span>
    </div>

    <div class="person">
      <p class="person-name">Dr. Helena Varga</p>
      <p class="person-title">Managing Director</p>
    </div>

    <div class="divider"></div>

    <ul class="contact-list">
      <li class="contact-item">
        <svg class="contact-icon" viewBox="0 0 24 24"><path d="M6 2l4 4-2 3c1 3 4 6 7 7l3-2 4 4-3 4C10 22 2 14 2 5z" fill="var(--accent-red)"/></svg>
        <span>323-555-0142</span>
      </li>
      <li class="contact-item">
        <svg class="contact-icon" viewBox="0 0 24 24"><rect x="6" y="1" width="12" height="22" rx="2" fill="var(--accent-red)"/><rect x="8" y="4" width="8" height="10" fill="#fff"/></svg>
        <span>323-555-0187</span>
      </li>
      <li class="contact-item">
        <svg class="contact-icon" viewBox="0 0 24 24"><g fill="none" stroke="var(--accent-red)" stroke-width="2"><circle cx="12" cy="12" r="10"/><ellipse cx="12" cy="12" rx="4.5" ry="10"/><path d="M2 12h20M4 7h16M4 17h16"/></g></svg>
        <span>www.larkmoorbio.com</span>
      </li>
      <li class="contact-item">
        <svg class="contact-icon" viewBox="0 0 24 24"><path d="M12 2L1 12h3v10h6v-6h4v6h6V12h3z" fill="var(--accent-red)"/></svg>
        <span class="contact-address">4217 NE 14th Ave Suite 7,<br>Gainesville Fl 32609</span>
      </li>
    </ul>
  </main>
</body>
</html>
```